CORAL DRIFT LODGE GRAND OPENING

We are the new owners and just finished completely remodeling our property and rooms in January 2017. To attract new customers we are planning a HOTEL GRAND OPENING PARTY on FEBRUARY 16 , 2017. EVENT WILL START WITH A 5:00PM HAPPY HOUR
WE WILL HAVE: LIVE MUSIC, SNACKS & BOOZE
The event will be a LUAU PARTY THEME

Industry/Entity Type

Property

Font styles to use
Sans Serif

Colors
85cae6
3176b5
ee3036
cadf82
fbed22
fece3e

Requirements
Must have
• property address:
• 4127 Marlow Lane
• St Pete Beach, Fl 33419
• COMPANY LOGO

```html
<!DOCTYPE html>
<html lang="en">
<head>
<meta charset="utf-8">
<title>Coral Drift Lodge – Grand Opening Party</title>
<link href="https://fonts.googleapis.com/css2?family=Montserrat:wght@500;600;700;800;900&display=swap" rel="stylesheet">
<style>
  :root {
    --sky: #85cae6;
    --ocean: #3176b5;
    --coral-red: #ee3036;
    --lime: #cadf82;
    --lemon: #fbed22;
    --sun: #fece3e;
    --orange: #f07a1a;
    --ink: #2a2a2a;
    --paper: #ffffff;
    --backdrop: #e6e2dc;
  }
  * { box-sizing: border-box; margin: 0; padding: 0; }
  html, body {
    width: 1200px; height: 1000px; overflow: hidden;
    background: var(--backdrop);
    font-family: "Montserrat", Arial, sans-serif;
  }
  .poster {
    position: absolute; left: 295px; top: 28px;
    width: 612px; height: 944px;
    background: var(--paper);
    overflow: hidden;
    box-shadow: 0 4px 14px rgba(0,0,0,.18);
  }
  .header {
    position: absolute; left: 0; top: 0; width: 612px; height: 105px;
    background: var(--lime);
  }
  .title {
    position: absolute; left: 27px; top: 32px; width: 565px;
    text-align: left; white-space: nowrap;
    font-weight: 900; font-size: 38px; letter-spacing: 0;
    line-height: 1;
    color: var(--coral-red);
    z-index: 5;
    text-shadow: 2px 0 var(--lemon), -2px 0 var(--lemon), 0 2px var(--lemon), 0 -2px var(--lemon),
                 2px 2px var(--lemon), -2px -2px var(--lemon), 2px -2px var(--lemon), -2px 2px var(--lemon);
  }
  .flower-art {
    position: absolute; left: 495px; top: 28px; width: 100px; height: 90px;
    border-radius: 50%;
    background: radial-gradient(circle at 35% 60%, #e3368a 0 26%, #b27ed8 42%, #6fd6e6 70%, rgba(111,214,230,0) 72%);
    z-index: 3;
  }
  .photo { position: absolute; }
  .photo-pool {
    left: 0; top: 105px; width: 612px; height: 302px;
    background: linear-gradient(180deg, #d9d7d2 0%, #b9a48a 28%, #3f4a3c 45%, #2c3a2d 60%, #8e8f8d 72%, #6d7f88 100%);
  }
  .divider { position: absolute; left: 0; top: 407px; width: 612px; height: 5px; background: var(--lime); }
  .photo-aerial {
    left: 0; top: 412px; width: 612px; height: 210px;
    background: linear-gradient(160deg, #a9c6d6 0%, #9fcfe2 35%, #5d7a5a 60%, #4f5a55 80%, #8f9296 100%);
  }
  .gallery-band { position: absolute; left: 0; top: 622px; width: 612px; height: 135px; background: var(--sky); }
  .photo-bedroom {
    left: 0; top: 627px; width: 150px; height: 123px;
    background: linear-gradient(180deg, #d8d6d0 0%, #c9c2b6 50%, #f3f2ef 70%, #a88e6e 100%);
  }
  .photo-lounge {
    left: 160px; top: 627px; width: 240px; height: 123px;
    clip-path: polygon(28% 0, 100% 0, 100% 100%, 0 100%);
    background: linear-gradient(180deg, #e8e6e1 0%, #cfcdc8 45%, #7f8491 65%, #b49c7e 100%);
  }
  .photo-sunset {
    left: 405px; top: 627px; width: 207px; height: 123px;
    clip-path: polygon(4% 0, 100% 0, 100% 100%, 0 100%);
    background: linear-gradient(180deg, #8b9cb6 0%, #d9a38a 30%, #f28b2b 50%, #3a2a2a 70%, #4a4a50 100%);
  }
  .badge { position: absolute; z-index: 4; }
  .badge svg { position: absolute; inset: 0; width: 100%; height: 100%; }
  .badge-text {
    position: absolute; inset: 0; display: flex; flex-direction: column;
    align-items: center; justify-content: center; text-align: center;
  }
  .event-badge { left: 435px; top: 140px; width: 130px; height: 130px; }
  .event-badge .badge-text { font-weight: 600; font-size: 15px; line-height: 1.15; color: var(--sky); }
  .event-badge .date { color: #ffffff; font-weight: 700; margin-bottom: 8px; }
  .event-badge .time { color: #ffffff; font-weight: 700; }
  .extras-badge { left: 25px; top: 330px; width: 152px; height: 152px; }
  .extras-badge .badge-text { font-weight: 800; font-size: 16px; line-height: 1.15; color: var(--coral-red); }
  .theme-badge { left: 443px; top: 500px; width: 146px; height: 146px; }
  .theme-badge .badge-text { font-weight: 800; font-size: 17px; line-height: 1.2; color: #ffffff; }
  .theme-badge .luau { font-size: 20px; font-weight: 900; }
  .brand {
    position: absolute; left: 40px; top: 790px; width: 220px;
    display: flex; flex-direction: column; align-items: center;
  }
  .brand-dot { width: 46px; height: 46px; border-radius: 50%; background: var(--sun); margin-bottom: 16px; }
  .brand-name { font-weight: 700; font-size: 19px; color: var(--ocean); letter-spacing: 0.5px; white-space: nowrap; }
  .contact {
    position: absolute; right: 35px; top: 772px; text-align: right;
    font-weight: 500; font-size: 15px; line-height: 1.2; color: var(--ink);
    font-style: normal;
  }
  .contact .web { margin-top: 12px; }
  .renovated {
    position: absolute; right: 35px; top: 866px; text-align: right;
    font-weight: 800; font-size: 16.5px; line-height: 1.1; color: var(--orange);
  }
</style>
</head>
<body>
  <main class="poster">
    <header class="header">
      <h1 class="title">GRAND OPENING PARTY</h1>
    </header>
    <div class="flower-art" role="img" aria-label="Cluster of tropical hibiscus flowers in pink, purple and aqua"></div>

    <div class="photo photo-pool" role="img" aria-label="Pool deck at dusk with lounge chairs, palm trees and a fountain statue"></div>
    <div class="divider"></div>
    <div class="photo photo-aerial" role="img" aria-label="Aerial view of the light blue lodge buildings, pool and parking lot"></div>

    <div class="gallery-band"></div>
    <div class="photo photo-bedroom" role="img" aria-label="Renovated bedroom with white bedding and dresser"></div>
    <div class="photo photo-lounge" role="img" aria-label="Renovated living area with grey sofa and dining table"></div>
    <div class="photo photo-sunset" role="img" aria-label="Orange sunset behind palm trees"></div>

    <div class="badge event-badge">
      <svg viewBox="0 0 130 130"><circle cx="65" cy="65" r="62" fill="var(--ocean)" stroke="#ffffff" stroke-width="4"/></svg>
      <div class="badge-text">
        <span>EVENT DATE</span>
        <span class="date">02/16/2017</span>
        <span>HAPPY HOUR</span>
        <span class="time">5:00 PM</span>
      </div>
    </div>

    <div class="badge extras-badge">
      <svg viewBox="-1.05 -1.05 2.1 2.1"><polygon fill="var(--sun)" points="1,0 .792,.212 .866,.5 .58,.58 .5,.866 .212,.792 0,1 -.212,.792 -.5,.866 -.58,.58 -.866,.5 -.792,.212 -1,0 -.792,-.212 -.866,-.5 -.58,-.58 -.5,-.866 -.212,-.792 0,-1 .212,-.792 .5,-.866 .58,-.58 .866,-.5 .792,-.212"/></svg>
      <div class="badge-text">
        <span>LIVE MUSIC</span>
        <span>SNACKS</span>
        <span>&amp;</span>
        <span>BOOZE</span>
      </div>
    </div>

    <div class="badge theme-badge">
      <svg viewBox="-1.05 -1.05 2.1 2.1"><polygon fill="var(--coral-red)" stroke="#ffffff" stroke-width=".04" points="1,0 .792,.212 .866,.5 .58,.58 .5,.866 .212,.792 0,1 -.212,.792 -.5,.866 -.58,.58 -.866,.5 -.792,.212 -1,0 -.792,-.212 -.866,-.5 -.58,-.58 -.5,-.866 -.212,-.792 0,-1 .212,-.792 .5,-.866 .58,-.58 .866,-.5 .792,-.212"/></svg>
      <div class="badge-text">
        <span>PARTY</span>
        <span>THEME</span>
        <span class="luau">: LUAU</span>
      </div>
    </div>

    <div class="brand">
      <div class="brand-dot"></div>
      <div class="brand-name">CORAL DRIFT LODGE</div>
    </div>

    <address class="contact">
      <div>4127 Marlow Lane</div>
      <div>St Pete Beach, Fl 33419</div>
      <div class="web">www.coraldriftlodge.com</div>
      <div>727 555-0148</div>
    </address>

    <p class="renovated">PROPERTY HAS<br>RECENTLY BEEN<br>COMPLETELY RENOVATED</p>
  </main>
</body>
</html>
```